Rapidly Expanding Real Estate Firm Seeking Signage Designs for Multiple Properties

We would like a sign design template created that we can use at our apartment buildings. We would like a consistent sign appearance that is adaptable enough to be used at different locations, on different mediums, and in different sizes. All vary for signage depending on the local laws and regulations as well as the type and style of the property. But the sign design should be consistent enough to support our company's branding efforts; so people that see our sign know its our company but also that the specific property is unique. Our thought was to incorporate the property address; i.e. "418 Birch" along with a portion of our company logo(attached). Then tag our website address across the bottom. Or some combination of that structure/design. It may make sense to just use the address and website address across the bottom OR it might be good to say 418 Birch St in large font with "by Amber Ridge Holdings Group" underneath as sort of a tag line. Not quite sure.
But we definitely want the signage to be clearly visible, professional, and clean. Easily read for the street. Should be flexible enough to work on metal or wood or any other medium with updates for the address and maybe color.
This is not a for sale sign design request. The sign concept will be used at apartment buildings. Sample property photos are attached - we are looking for a design template that is flexible enough to work on various property types. Also could be wall mounted or a pylon sign. Concept should work either way.

Target Market(s)

Prospective Tenants 25-45 yrs of age with incomes ranging from $55k - $95k.

Industry/Entity Type

Real Estate - Apartments

Colors
59FF00
82FF00
B8FF75
E3FFCB
F4FFEA

Requirements
Must have
• The street address number, web address(www.amberridgeholdingsgroup.com), & incorporate our primary colors(green,white,black)
Nice to have
• "418 Birch St." by Amber Ridge
Should not have
• Should not say For Sale, For Lease, post our phone number.

```html
<!DOCTYPE html>
<html lang="en">
<head>
<meta charset="utf-8">
<title>418 Birch Street — Property Sign</title>
<link rel="stylesheet" href="https://fonts.googleapis.com/css2?family=Cinzel:wght@500;600&family=Poppins:wght@600&display=swap">
<style>
  :root {
    --backdrop: #4a4849;
    --sign-light: #ffffff;
    --sign-edge: #d6d6d6;
    --ink: #000000;
    --brand-green: #4f8f1c;
    --brand-green-soft: #97c865;
  }
  html, body {
    margin: 0;
    padding: 0;
    width: 1200px;
    height: 1200px;
    overflow: hidden;
    background: var(--backdrop);
  }
  .property-sign {
    position: absolute;
    left: 200px;
    top: 0;
    width: 800px;
    height: 1200px;
    background: radial-gradient(ellipse 60% 75% at 50% 50%, var(--sign-light) 0%, #f2f2f2 45%, var(--sign-edge) 100%);
    overflow: hidden;
  }
  .sign-type {
    position: absolute;
    inset: 0;
    width: 800px;
    height: 1200px;
  }
  .street-number, .street-name, .byline {
    font-family: "Cinzel", "Times New Roman", serif;
    fill: var(--ink);
  }
  .street-number { font-weight: 600; font-size: 470px; }
  .street-name { font-weight: 600; font-size: 94px; }
  .byline { font-weight: 600; font-size: 58px; }
  .company-name, .web-address {
    font-family: "Poppins", "Helvetica", sans-serif;
    font-weight: 600;
  }
  .company-name { fill: var(--brand-green-soft); font-size: 30px; }
  .company-mark { fill: var(--brand-green-soft); }
  .web-address { fill: var(--brand-green); font-size: 38px; }
  .base-band {
    position: absolute;
    left: 0;
    bottom: 0;
    width: 800px;
    height: 15px;
    background: var(--ink);
  }
</style>
</head>
<body>
  <div class="property-sign">
    <svg class="sign-type" viewBox="0 0 800 1200" xmlns="http://www.w3.org/2000/svg">
      <text class="street-number" x="400" y="462" text-anchor="middle" textLength="672" lengthAdjust="spacingAndGlyphs">418</text>
      <text class="street-name" x="400" y="557" text-anchor="middle" textLength="674" lengthAdjust="spacing">BIRCH STREET</text>
      <text class="byline" x="400" y="669" text-anchor="middle">BY</text>

      <rect class="company-mark" x="700" y="905" width="70" height="70"/>
      <text class="company-name" x="770" y="1010" text-anchor="end">Amber Ridge</text>
      <text class="company-name" x="770" y="1046" text-anchor="end">Holdings Group</text>

      <text class="web-address" x="400" y="1104" text-anchor="middle" textLength="657" lengthAdjust="spacingAndGlyphs">www.amberridgeholdingsgroup.com</text>
    </svg>
    <div class="base-band"></div>
  </div>
</body>
</html>
```